Dental Office Needs a Flyer Design to Attract New Patients

We need a flyer design for a dental office in Rockville, MD, US. Our office name is Brightpath Dental Care. Our website is: brightpathdentalcare.example and our office logo can be seen on the website. We would like stay that call and make an appointment with Dr. Lena Okaru. The flyer can follow the color scheme of our logo (blue and white). We current have Holiday/New Year special: Dental exam, x-ray, and cleaning for $95 (a $300 value); please include this in the flyer. Also if you can include a winter inspired picture to be part of the flyer, that would be great. We really like your Grin Tallowby flyer design and are looking for something similar. Thank you!
Target Market(s)
Apartment complex that is 5 minutes (less than 1 mile away)
Industry/Entity Type
Dental
Look and feel

```html
<!DOCTYPE html>
<html lang="en">
<head>
<meta charset="utf-8">
<title>Brightpath Dental Care – Holiday/New Year Special</title>
<link rel="stylesheet" href="https://fonts.googleapis.com/css2?family=Open+Sans:wght@300;400;700;800&display=swap">
<style>
  :root {
    --teal-dark: #2a7382;
    --teal-text: #2b7a8a;
    --teal-logo: #3f9fb8;
    --band-top: #a9d6de;
    --band-bottom: #5bbccf;
    --grey-text: #8a8a8a;
    --white: #ffffff;
    --photo-light: #f4e3d8;
    --photo-red: #c8322a;
    --photo-dark: #5a3524;
  }
  * { margin: 0; padding: 0; box-sizing: border-box; }
  html, body { width: 928px; height: 1200px; overflow: hidden; background: var(--white); }
  body { font-family: "Open Sans", Arial, sans-serif; }

  .flyer { position: relative; width: 928px; height: 1200px; background: var(--white); overflow: hidden; }

  .hero-photo { position: absolute; left: 0; top: 0; width: 928px; height: 680px; }

  .brand {
    position: absolute; left: 62px; top: 72px;
    display: flex; align-items: center; gap: 14px;
  }
  .brand-dot { width: 40px; height: 40px; border-radius: 50%; background: var(--teal-logo); }
  .brand-name {
    font-size: 30px; font-weight: 800; line-height: 1.1; color: var(--teal-logo);
  }

  .dentist { position: absolute; left: 60px; top: 242px; color: var(--teal-text); }
  .dentist-name { font-size: 29px; font-weight: 700; line-height: 1.2; }
  .dentist-title { font-size: 19px; font-weight: 400; }

  .promo-band {
    position: absolute; left: 0; top: 678px; width: 928px; height: 388px;
    background: linear-gradient(to bottom, var(--band-top), var(--band-bottom));
  }

  .offer-card {
    position: absolute; left: 72px; top: 654px; width: 786px; height: 240px;
    background: var(--white);
  }
  .offer-heading {
    position: absolute; left: 40px; top: 42px;
    font-size: 49px; font-weight: 700; color: var(--teal-text); letter-spacing: -0.3px;
  }
  .offer-items {
    position: absolute; left: 38px; top: 134px;
    font-size: 31px; font-weight: 700; line-height: 1.25; color: var(--grey-text);
  }
  .offer-price {
    position: absolute; left: 400px; top: 140px;
    font-size: 56px; color: var(--teal-text); line-height: 1;
  }
  .offer-price .price-was { font-weight: 300; text-decoration: line-through; text-decoration-thickness: 3px; }
  .offer-price .price-for { font-weight: 300; }
  .offer-price .price-now { font-weight: 700; }

  .welcome {
    position: absolute; left: 72px; top: 940px; width: 790px;
    font-size: 17.5px; line-height: 1.35; color: var(--white);
  }

  .contact-bar {
    position: absolute; left: 0; top: 1066px; width: 928px; height: 134px;
    background: var(--teal-dark); color: var(--white);
    font-size: 23px; font-weight: 700; text-align: center;
  }
  .contact-line { position: absolute; left: 0; width: 100%; }
  .contact-line.first { top: 34px; }
  .contact-line.second { top: 68px; }
  .contact-line .gap { display: inline-block; width: 54px; }
</style>
</head>
<body>
<div class="flyer">

  <svg class="hero-photo" viewBox="0 0 928 680" role="img"
       aria-label="Winter holiday photo: smiling young woman in a red Santa hat and red sweater holding a red Christmas ornament">
    <defs>
      <linearGradient id="photoTone" x1="0" y1="0" x2="1" y2="1">
        <stop offset="0" stop-color="var(--photo-light)"/>
        <stop offset="0.55" stop-color="#e7b9a2"/>
        <stop offset="0.8" stop-color="var(--photo-red)"/>
        <stop offset="1" stop-color="var(--photo-dark)"/>
      </linearGradient>
    </defs>
    <path d="M400 0 H928 V680 H24 V340 H400 Z" fill="url(#photoTone)"/>
  </svg>

  <div class="brand">
    <span class="brand-dot"></span>
    <span class="brand-name">Brightpath<br>Dental Care</span>
  </div>

  <div class="dentist">
    <div class="dentist-name">Lena Okaru, D.D.S</div>
    <div class="dentist-title">General &amp; Cosmetic Dentist</div>
  </div>

  <div class="promo-band"></div>

  <div class="offer-card">
    <h1 class="offer-heading">Holiday/New Year special</h1>
    <p class="offer-items">Dental exam, x-ray<br>and cleaning</p>
    <p class="offer-price"><span class="price-for">for </span><span class="price-was">$300</span> <span class="price-now">$95</span></p>
  </div>

  <p class="welcome">We are always welcoming new patients and we would love to have you as part of our dental family. If you have any questions please call us.&nbsp; We love hearing from our patients and anyone who may be interested in becoming one.</p>

  <footer class="contact-bar">
    <div class="contact-line first">Ph: (30) 555-0147<span class="gap"></span>www.brightpathdentalcare.example</div>
    <div class="contact-line second">4410 Larkspur Lane, Rockville, MD 20852</div>
  </footer>

</div>
</body>
</html>
```